Copper Lantern - website for leadership service

I would like help to use a Squarespace template for a simple website.
We already have a logo which will influence the colour choice and tone.
Clean lines for executive audience. it is an exclusive service. I have all the content ready to go.
Would like some images included.

I will upload the content soon.

Does NOT need SEO as it will be direct mailed. Also does NOT need to consider having any payment pages or enquiry form.
Thanks

Target Market(s)

Women executives - senior leaders. Stylish, serious and capable.

Coding

Coded - Design and coding required

Number of Pages Required

3 page

Colors
3176b5
fee18a

Requirements
Must have
• Sqaurespace template. And scrolling down page format.

To suit style of the blue and gold logo.
Nice to have
• Simple, Stylish and exclusive feel. Inspiring but not "New Age"
Should not have
• Too many colours.

No

```html
<!DOCTYPE html>
<html lang="en">
<head>
<meta charset="utf-8">
<title>Copper Lantern</title>
<link rel="stylesheet" href="https://fonts.googleapis.com/css2?family=Playfair+Display:ital,wght@0,400;0,700;1,400;1,700&display=swap">
<style>
:root{
  --navy:#1b2440;
  --navy-deep:#161e36;
  --gold:#e4c97f;
  --gold-text:#a8873c;
  --butter:#fde08a;
  --ink:#1b2440;
  --body:#4a4f5c;
  --white:#ffffff;
  --dots:rgba(214,168,70,.18);
}
*{margin:0;padding:0;box-sizing:border-box}
html,body{width:1200px;height:5112px;overflow:hidden}
body{position:relative;background:var(--white);font-family:"Playfair Display",Georgia,serif;color:var(--ink)}
.abs{position:absolute}
.site-nav{position:absolute;left:0;width:1200px;height:100px;background:var(--navy)}
.brand{position:absolute;left:124px;top:36px;display:flex;align-items:center;gap:10px;color:var(--gold);font-size:15px;letter-spacing:2px;font-weight:400}
.brand-dot{width:14px;height:14px;border-radius:50%;background:var(--gold)}
.nav-links{position:absolute;top:40px;left:0;width:1200px;font-size:15px;color:var(--white)}
.nav-links span{position:absolute}
.nav-links .active{color:var(--gold)}
.hero{top:100px;left:0;width:1200px;height:490px;background:var(--gold)}
.hero-quote{left:168px;top:252px;width:420px;font-size:23px;line-height:33px;color:var(--ink)}
.hero-quote em{font-weight:700}
.qm{color:#f5d98a;font-weight:700}
.hero-author{left:383px;top:418px;font-size:21px;color:#8a6d2e}
.dots{background:var(--dots)}
.photo{background:linear-gradient(160deg,#b9b3aa,#7d766c)}
.about-title{left:648px;top:706px;font-size:28px;font-weight:700}
.about-text{left:650px;top:782px;width:450px;font-size:16.5px;line-height:22px;color:var(--body)}
.about-text p{margin-bottom:22px}
.quote-band{top:1360px;left:0;width:1198px;height:395px;background:var(--butter)}
.band-quote{left:486px;top:1468px;font-size:29px;line-height:36px;font-style:italic;font-weight:700;color:var(--ink)}
.band-author{left:515px;top:1624px;font-size:20px;font-weight:700;color:var(--gold-text)}
.page-head{left:0;width:1200px;background:var(--butter)}
.page-title{left:0;width:1200px;text-align:center;font-size:47px;font-weight:700}
.t-name{left:415px;font-size:26px}
.t-role{left:415px;font-size:18px;font-weight:700}
.t-quote{left:415px;width:640px;font-size:17.5px;line-height:23px;font-style:italic;color:var(--body)}
.t-quote .qm{font-style:normal}
.navy-box{background:var(--navy)}
.gold-box{background:var(--butter)}
.card-title{width:300px;font-size:17px;font-weight:700;line-height:22px}
.card-text{width:298px;font-size:14.5px;line-height:19px;color:var(--body)}
.read-more{width:110px;height:32px;background:var(--butter);font-size:14px;line-height:32px;text-align:center;color:var(--ink)}
.footer{left:0;top:4735px;width:1200px;height:290px;background:var(--navy)}
.footer-brand{left:134px;top:4898px;width:260px;text-align:center;color:var(--white);font-size:21px;letter-spacing:2px}
.footer-sub{left:134px;top:4933px;width:260px;text-align:center;color:var(--white);font-size:12px;letter-spacing:2px}
.footer-dot{left:250px;top:4846px;width:28px;height:28px;border-radius:50%;background:var(--gold)}
.f-head{font-size:19px;font-weight:700;color:var(--gold)}
.f-links{left:555px;top:4858px;font-size:15px;line-height:19px;color:var(--white)}
.social{width:34px;height:34px;border-radius:50%;background:var(--white)}
.copyright{left:0;top:5025px;width:1200px;height:87px;background:var(--navy-deep);text-align:center;line-height:87px;color:#b8bccb;font-size:15px}
</style>
</head>
<body>

<!-- Home / About page -->
<header class="site-nav" style="top:0">
  <div class="brand"><span class="brand-dot"></span>COPPER LANTERN</div>
  <nav class="nav-links"><span style="left:637px">Home</span><span class="active" style="left:711px">About</span><span style="left:783px">Testimonials</span><span style="left:905px">Resources</span><span style="left:1008px">Contact</span></nav>
</header>

<section class="abs hero"></section>
<p class="abs hero-quote"><span class="qm">“</span><em>COPPER LANTERN</em> catalyses our best women leaders, getting them to the forefront of this exciting new wave of business approaches and success<span class="qm">”</span></p>
<p class="abs hero-author">Marian Hale</p>
<div class="abs dots" role="img" aria-label="Dot pattern" style="left:388px;top:455px;width:130px;height:130px"></div>
<div class="abs" role="img" aria-label="Portrait of Marian Hale seated, with a gold ring motif behind her" style="left:670px;top:110px;width:460px;height:480px;background:radial-gradient(ellipse at 55% 45%,#9c958a 0%,#c9b36f 60%,var(--gold) 100%)"></div>

<div class="abs dots" role="img" aria-label="Dot pattern" style="left:70px;top:1065px;width:126px;height:260px"></div>
<div class="abs gold-box" style="left:110px;top:730px;width:365px;height:535px;background:var(--butter)"></div>
<div class="abs photo" role="img" aria-label="Portrait of Marian Hale in a patterned scarf" style="left:200px;top:685px;width:375px;height:538px"></div>
<h2 class="abs about-title">About Marian</h2>
<div class="abs about-text">
  <p>Marian is a highly experienced executive coach, business woman and thought leader in leadership for change. She is widely respected for her astute commercial and strategic acumen.</p>
  <p>Marian believes that commercial businesses are one of the most powerful driving forces for positive change in the world. She has built her decades-long career in executive coaching helping strong, capable executives succeed on their own terms She has a particular interest in championing women’s role in redefining business.</p>
  <p>Marian lives in New Zealand, enjoys spending time with her family, swimming in the ocean and growing vegetables at home on Kauri Island, where she has lived for 25 years. She is grateful to be living in a safe and abundant part of the world.</p>
</div>

<section class="abs quote-band"></section>
<div class="abs dots" role="img" aria-label="Dot pattern" style="left:205px;top:1555px;width:265px;height:125px"></div>
<div class="abs photo" role="img" aria-label="Portrait of Nadira Vale" style="left:152px;top:1427px;width:210px;height:216px;background:linear-gradient(160deg,#8a857d,#4b4741)"></div>
<p class="abs band-quote"><span class="qm" style="font-style:normal">“</span>Another world is not only possible;<br>she is on her way.<br>On a quiet day, I can hear her breathing<span class="qm" style="font-style:normal">”</span></p>
<p class="abs band-author">Nadira Vale</p>

<!-- Testimonials page -->
<header class="site-nav" style="top:1755px">
  <div class="brand"><span class="brand-dot"></span>COPPER LANTERN</div>
  <nav class="nav-links"><span style="left:637px">Home</span><span style="left:711px">About</span><span class="active" style="left:783px">Testimonials</span><span style="left:905px">Resources</span><span style="left:1008px">Contact</span></nav>
</header>
<section class="abs page-head" style="top:1855px;height:230px"></section>
<h1 class="abs page-title" style="top:1946px">Testimonials</h1>
<div class="abs dots" role="img" aria-label="Dot pattern" style="left:470px;top:2020px;width:260px;height:125px"></div>

<div class="abs dots" role="img" aria-label="Dot pattern" style="left:95px;top:2222px;width:260px;height:70px"></div>
<div class="abs gold-box" style="left:115px;top:2262px;width:210px;height:210px"></div>
<div class="abs navy-box" role="img" aria-label="Photo of Nadira Vale" style="left:132px;top:2250px;width:210px;height:210px"></div>
<h3 class="abs t-name" style="top:2244px;font-weight:400">Nadira Vale</h3>
<p class="abs t-role" style="top:2282px">CEO at Kerrow Trust</p>
<p class="abs t-quote" style="top:2325px"><span class="qm" style="margin-left:-32px">“</span> I have had the pleasure of spending the last year working with Marian. Her measured guidance has been a pillar for my success this year. She helped me to find my voice and gave me the confidence to speak up where needed. Marian has helped me to prioritise my vision to become more of a leader and less of an administrator. I feel so much more confident in my role with a clear vision into the future. <span class="qm">”</span></p>

<div class="abs dots" role="img" aria-label="Dot pattern" style="left:95px;top:2530px;width:260px;height:70px"></div>
<div class="abs gold-box" style="left:115px;top:2570px;width:210px;height:210px"></div>
<div class="abs navy-box" role="img" aria-label="Photo of Jodie Carrow" style="left:132px;top:2558px;width:210px;height:210px"></div>
<h3 class="abs t-name" style="top:2552px;font-weight:400">Jodie Carrow</h3>
<p class="abs t-role" style="top:2590px">General Manager - New Zealand at Keel Batteries / Keel Glass</p>
<p class="abs t-quote" style="top:2633px"><span class="qm" style="margin-left:-32px">“</span> I had the pleasure of being able to enjoy the benefits of executive coaching with Marian. The insights and guidance Marian provided into my development has helped me immensely both personally and professionally and I can’t recommend her enough for any person wanting to move forward with their journey <span class="qm">”</span></p>

<div class="abs dots" role="img" aria-label="Dot pattern" style="left:95px;top:2837px;width:260px;height:70px"></div>
<div class="abs gold-box" style="left:115px;top:2877px;width:210px;height:210px"></div>
<div class="abs navy-box" role="img" aria-label="Photo of Tessa Wynford" style="left:132px;top:2865px;width:210px;height:210px"></div>
<h3 class="abs t-name" style="top:2859px;font-weight:400">Tessa Wynford</h3>
<p class="abs t-role" style="top:2897px">Chief Executive Officer at The Harbour Property Institute</p>
<p class="abs t-quote" style="top:2940px"><span class="qm" style="margin-left:-32px">“</span> Marian has a style of coaching that is both supportive and challenging. Her style helps explore the possible in a planned and constructive manner - helping to push you forward and widen your perspective. Very valuable discussions. <span class="qm">”</span></p>

<!-- Resources page -->
<header class="site-nav" style="top:3180px">
  <div class="brand"><span class="brand-dot"></span>COPPER LANTERN</div>
  <nav class="nav-links"><span style="left:637px">Home</span><span style="left:711px">About</span><span style="left:783px">Testimonials</span><span class="active" style="left:905px">Resources</span><span style="left:1008px">Contact</span></nav>
</header>
<section class="abs page-head" style="top:3280px;height:215px"></section>
<h1 class="abs page-title" style="top:3360px">Related Resources</h1>
<div class="abs dots" role="img" aria-label="Dot pattern" style="left:470px;top:3505px;width:260px;height:115px"></div>

<div class="abs gold-box" style="left:112px;top:3602px;width:298px;height:181px"></div>
<div class="abs navy-box" role="img" aria-label="Resource image" style="left:122px;top:3612px;width:298px;height:181px"></div>
<h4 class="abs card-title" style="left:125px;top:3810px">Business Leaders Forum 2019</h4>
<p class="abs card-text" style="left:125px;top:3880px">Business Leaders Forum today announced the release of a new Statement on the Purpose of a Corporation signed by 181 CEOs who commit to lead their companies for the benefit of all stakeholders’ customers, employees, suppliers, communities and shareholders.</p>
<div class="abs read-more" style="left:125px;top:4049px">Read More</div>

<div class="abs gold-box" style="left:442px;top:3602px;width:298px;height:181px"></div>
<div class="abs navy-box" role="img" aria-label="Resource image" style="left:452px;top:3612px;width:298px;height:181px"></div>
<h4 class="abs card-title" style="left:455px;top:3810px">Celia Marsh | Founder<br>CEO | Bloomwell</h4>
<p class="abs card-text" style="left:455px;top:3880px">Why are we spending untold energy trying to work our way up the ladder of a broken system? Instead of dreaming of 50/50 representation in a suboptimal system, why don’t we instead envision and build a new and better one?</p>
<div class="abs read-more" style="left:455px;top:4049px">Read More</div>

<div class="abs gold-box" style="left:773px;top:3602px;width:298px;height:181px"></div>
<div class="abs navy-box" role="img" aria-label="Resource image" style="left:783px;top:3612px;width:298px;height:181px"></div>
<h4 class="abs card-title" style="left:786px;top:3810px">Renée Talbot | CEO | HERA</h4>
<p class="abs card-text" style="left:786px;top:3880px">Women are redefining leadership into something that is values-based, shifting the way power is expressed and affecting the global culture. Rather than trying to fit women into the existing models and systems and level the playing field, we are creating an entirely new field</p>
<div class="abs read-more" style="left:786px;top:4049px">Read More</div>

<div class="abs gold-box" style="left:112px;top:4150px;width:298px;height:181px"></div>
<div class="abs navy-box" role="img" aria-label="Resource image" style="left:122px;top:4160px;width:298px;height:181px"></div>
<h4 class="abs card-title" style="left:125px;top:4358px">Owen Pritchard, Chairman CEO |<br>Pritchard &amp; Lowe</h4>
<p class="abs card-text" style="left:125px;top:4430px">the essential role corporations can play in improving our society when CEOs are truly committed to meeting the needs of all stakeholders</p>
<div class="abs read-more" style="left:125px;top:4622px">Read More</div>

<div class="abs gold-box" style="left:442px;top:4150px;width:298px;height:181px"></div>
<div class="abs navy-box" role="img" aria-label="Resource image" style="left:452px;top:4160px;width:298px;height:181px"></div>
<h4 class="abs card-title" style="left:455px;top:4358px">Dana Whitcombe | former chief<br>talent officer | Streamline</h4>
<p class="abs card-text" style="left:455px;top:4430px">Organizations need to completely rethink what they are about and what it means to lead. It’s not about one person or even those residing at the top anymore. In today’s world, everyone has to adopt a leadership mindset.</p>
<div class="abs read-more" style="left:455px;top:4622px">Read More</div>

<div class="abs gold-box" style="left:773px;top:4150px;width:298px;height:181px"></div>
<div class="abs navy-box" role="img" aria-label="Resource image" style="left:783px;top:4160px;width:298px;height:181px"></div>
<h4 class="abs card-title" style="left:786px;top:4358px">Martin Kessel<br>CEO | CloudCart</h4>
<p class="abs card-text" style="left:786px;top:4430px">The “new capitalism” happens when companies act on behalf of both shareholders and stakeholders, as doing well and doing good converge. “In the years to come,” he writes, “the principles we live by, and how we discuss them and apply them, will be the essential function of any thriving business.</p>
<div class="abs read-more" style="left:786px;top:4622px">Read More</div>

<!-- Footer -->
<footer class="abs footer"></footer>
<div class="abs footer-dot"></div>
<p class="abs footer-brand">COPPER LANTERN</p>
<p class="abs footer-sub">RADICAL LEADERSHIP COACHING</p>
<h5 class="abs f-head" style="left:555px;top:4812px">Overview</h5>
<div class="abs f-links">About Us<br>Testimonials<br>Resources<br>Contact</div>
<h5 class="abs f-head" style="left:852px;top:4812px">Join our social media</h5>
<div class="abs social" role="img" aria-label="Social link" style="left:895px;top:4863px"></div>
<div class="abs social" role="img" aria-label="Social link" style="left:942px;top:4863px"></div>
<div class="abs social" role="img" aria-label="Social link" style="left:990px;top:4863px"></div>
<div class="abs copyright">© Copyright 2020 COPPER LANTERN. All Rights Reserved</div>

</body>
</html>
```